Boutique custom software development company needs new business card

Our nearly 20 year old custom software development company would like to better include the fact that we are now providing Bitcoin services. These new services are B2B include education (how to acquire and securely hold Bitcoin) and integrating Bitcoin payments into existing ecommerce sites or other existing systems. Please keep the card clean and simple. Attached is our current design and some other files. vexalon.example

Target Market(s)

businesses owners interested in long term relationship

Industry/Entity Type

Custom software development and Bitcoin

Contact Information for Business Card

Marcus Ellwood, marcus@vexalon.example, vexalon.example, (888) 555-VEXAL

Font styles to use
Other font styles liked:
• monospace

Requirements
Must have
• double-sided
Nice to have
• clean and simple
Should not have
• physical address

```html
<!DOCTYPE html>
<html lang="en">
<head>
<meta charset="utf-8">
<title>Vexalon Business Card</title>
<link href="https://fonts.googleapis.com/css2?family=Fira+Sans+Condensed:wght@600;700&family=Roboto+Mono:wght@400;700&display=swap" rel="stylesheet">
<style>
  :root {
    --page: #d6d6d6;
    --card-blue: #232f8c;
    --accent-orange: #f5a01e;
    --ink-white: #ffffff;
    --divider: rgba(255, 255, 255, 0.35);
    --icon-glow: #8fb0ff;
    --icon-core: #e9efff;
  }
  * { box-sizing: border-box; margin: 0; padding: 0; }
  html, body {
    width: 1200px;
    height: 846px;
    overflow: hidden;
    background: var(--page);
  }
  .sheet {
    position: relative;
    width: 1200px;
    height: 846px;
  }
  .card {
    position: absolute;
    top: 268px;
    width: 540px;
    height: 309px;
    background: var(--card-blue);
    overflow: hidden;
    box-shadow: 0 10px 30px rgba(0, 0, 0, 0.18);
  }
  .card--front { left: 40px; }
  .card--back { left: 620px; }

  /* Front side */
  .brand-name {
    position: absolute;
    font-family: "Fira Sans Condensed", sans-serif;
    font-weight: 700;
    letter-spacing: 1px;
  }
  .card--front .brand-name {
    left: 34px;
    top: 56px;
    font-size: 46px;
    color: var(--ink-white);
  }
  .contact-divider {
    position: absolute;
    left: 236px;
    top: 44px;
    width: 1px;
    height: 80px;
    background: var(--divider);
  }
  .contact {
    position: absolute;
    left: 252px;
    top: 46px;
    font-family: "Roboto Mono", monospace;
    color: var(--ink-white);
    font-size: 13px;
    line-height: 19px;
  }
  .contact__name {
    color: var(--accent-orange);
    font-weight: 700;
    font-size: 15px;
  }
  .services {
    position: absolute;
    left: 20px;
    right: 20px;
    top: 150px;
    display: flex;
    justify-content: space-between;
  }
  .service {
    width: 118px;
    display: flex;
    flex-direction: column;
    align-items: center;
  }
  .service__art {
    width: 62px;
    height: 62px;
    border-radius: 50%;
    background: radial-gradient(circle at 45% 40%, var(--icon-core) 0%, var(--icon-glow) 45%, rgba(35, 47, 140, 0) 75%);
  }
  .service__label {
    margin-top: 8px;
    font-family: "Fira Sans Condensed", sans-serif;
    font-weight: 600;
    font-size: 12px;
    line-height: 13px;
    text-transform: uppercase;
    text-align: center;
    color: var(--accent-orange);
  }
  .accent-band {
    position: absolute;
    left: 0;
    right: 0;
    bottom: 16px;
    height: 9px;
    background: var(--accent-orange);
  }

  /* Back side */
  .card--back .brand-name {
    left: 0;
    right: 0;
    top: 100px;
    text-align: center;
    font-size: 74px;
    line-height: 1;
    color: var(--accent-orange);
  }
  .back-url {
    position: absolute;
    left: 0;
    right: 0;
    top: 190px;
    text-align: center;
    font-family: "Fira Sans Condensed", sans-serif;
    font-weight: 700;
    font-size: 18px;
    letter-spacing: 0.5px;
    color: var(--accent-orange);
  }
</style>
</head>
<body>
<main class="sheet">
  <section class="card card--front" aria-label="Business card front">
    <div class="brand-name">VEXALON</div>
    <div class="contact-divider"></div>
    <div class="contact">
      <p class="contact__name">Marcus Ellwood</p>
      <p>(888) 555-VEXAL</p>
      <p>marcus@vexalon.example</p>
      <p>www.vexalon.example</p>
    </div>
    <div class="services">
      <div class="service">
        <div class="service__art" role="img" aria-label="Illustration of an app toggle panel"></div>
        <p class="service__label">Web &amp; Native<br>Applications</p>
      </div>
      <div class="service">
        <div class="service__art" role="img" aria-label="Illustration of a round robot helper"></div>
        <p class="service__label">Digital Process<br>Automation</p>
      </div>
      <div class="service">
        <div class="service__art" role="img" aria-label="Illustration of a data cloud"></div>
        <p class="service__label">Cloud-Based<br>Portals</p>
      </div>
      <div class="service">
        <div class="service__art" role="img" aria-label="Illustration of a glowing brain"></div>
        <p class="service__label">Bitcoin<br>Consulting</p>
      </div>
    </div>
    <div class="accent-band"></div>
  </section>

  <section class="card card--back" aria-label="Business card back">
    <div class="brand-name">VEXALON</div>
    <p class="back-url">WWW.VEXALON.EXAMPLE</p>
  </section>
</main>
</body>
</html>
```